Wholesale e-commerce website re-design

We are a wholesaler of African-made and African-themed products, and we're looking to update the look and feel of our website www.lomatrade.com to improve user experience. We'd like to have a cleaner homepage that keeps the product category menus (but simplifies them), allows certain products to be featured, and has a simple CTA box (something like "Login" for existing wholesale customers or "Start a Business" for new customers). The layout might be something along the lines of http://www.pinewellmarket.com/ except with a shopping cart featured at the top right. Our colors tend to be earth-toned, but the current color palate looks dated. Also see our blog.lomatrade.com page for themes and color ideas that are maybe more up-to-date. On our product pages, we want to feature the products more prominently and have simpler, cleaner Buy or Add buttons.

Other reference sites for inspiration: dravensupply.com, kettlorhome.com, http://www.pinewellmarket.com, http://morvanbulkgoods.com/ http://tenubra.com/
Updates

Project Deadline Extended
Reason: We like many of the designs that have been submitted so far, but need more time to make our final choice.

Target Market(s)

Small wholesale customers, most have a small business or home-based business. Also some retail, so an option for retail customers to click at the top to see retail pricing would be nice

Industry/Entity Type

Wholesale

Number of Pages Required

3 page

Font styles to use
Sans Serif

Requirements
Must have
• Clean, clear design that highlights products and reduces friction to customer purchase. Should include one homepage, one product page, and one shopping cart page design. Works with all browser types and be mobile-friendly.
Nice to have
• Other color schemes that would look good with our logo (maybe different from colors chosen below).
Should not have
• Splash pages with special effects, Adobe flash, elements that slow down page load times or that only work well in certain browsers.

```html
<!DOCTYPE html>
<html lang="en">
<head>
<meta charset="utf-8">
<title>Loma Trade – Wholesale African Goods</title>
<link rel="stylesheet" href="https://fonts.googleapis.com/css2?family=Questrial&family=Cabin:wght@400;600;700&display=swap">
<style>
:root{
  --red:#c9413a;
  --ink:#222;
  --line:#cfcfcf;
  --hero-bg:#d6d6d6;
}
*{box-sizing:border-box;margin:0;padding:0}
html,body{width:1200px;height:1174px;overflow:hidden;background:#fff}
body{position:relative;font-family:"Questrial",sans-serif;color:var(--ink)}
.abs{position:absolute}
.topbar{left:0;top:0;width:1188px;height:43px;background:var(--red);color:#fff;font-size:13.5px}
.topbar .phone{left:103px;top:11px;font-family:"Cabin",sans-serif;font-weight:600;font-size:17px;display:flex;align-items:center;gap:9px}
.toplinks{right:88px;top:13px;display:flex;align-items:center;list-style:none}
.toplinks li{padding:0 15px;border-left:1px solid rgba(255,255,255,.8);line-height:14px;display:flex;align-items:center;gap:6px}
.toplinks li:first-child{border-left:0}
.brand-name{left:104px;top:90px;font-family:"Cabin",sans-serif;font-weight:700;font-size:22px;color:#222;letter-spacing:1px}
.brand-dot{left:160px;top:124px;width:12px;height:12px;border-radius:50%;background:var(--red)}
.search{left:502px;top:60px;width:202px;height:31px;border:1px solid #ccc;font-size:13.5px;color:#555;padding:7px 11px}
.search svg{position:absolute;right:8px;top:8px}
.social{top:61px;display:flex;gap:9px;left:736px}
.social span,.fsocial span{width:31px;height:31px;border:1.5px solid var(--red);border-radius:50%;display:flex;align-items:center;justify-content:center}
.support{left:911px;top:60px;width:190px;height:31px;background:#d9d9d9;border-radius:3px;font-size:13px;padding:8px 0 0 8px;display:flex;gap:6px}
.mainnav{left:242px;top:143px;display:flex;list-style:none;font-size:16.5px}
.mainnav li{margin-right:26px}
.mainnav li.active{color:var(--red)}
.hero{left:99px;top:178px;width:690px;height:472px;background:var(--hero-bg)}
.hero-photo{left:0;top:40px;width:440px;height:432px;background:linear-gradient(90deg,#e46a1e 0%,#f08a2a 35%,#7a2b6a 60%,#5a1d55 100%);border-radius:40% 40% 0 0 / 20% 20% 0 0}
.hero-copy{right:11px;top:167px;text-align:right;font-size:24.5px;line-height:27px;color:#222;font-weight:400}
.btn-red{background:var(--red);color:#fff;font-family:"Cabin",sans-serif;font-weight:600;border-radius:3px}
.hero-btn{right:11px;top:296px;width:104px;height:31px;font-size:16px;text-align:center;padding-top:5px}
.dots{right:18px;top:344px;display:flex;gap:4px}
.dots span{width:11px;height:11px;border-radius:50%;background:var(--red);border:1.5px solid #8a2a25}
.promo{left:800px;top:178px;width:300px;height:472px;background:var(--red);color:#fff;text-align:center}
.promo h2{font-family:"Cabin",sans-serif;font-weight:700;font-size:16px;line-height:21px;margin-top:8px}
.promo-photo{left:7px;top:57px;width:286px;height:224px;border:2px solid #f0d8d5;background:linear-gradient(180deg,#cfc4ae 0%,#b7a888 55%,#d8d4cc 100%)}
.promo p{font-size:13.5px;line-height:16px;padding:0 8px}
.promo .p1{left:0;top:294px;width:100%}
.promo .p2{left:0;top:321px;width:100%}
.promo .p3{left:0;top:378px;width:100%}
.promo-btn{left:59px;top:430px;width:182px;height:31px;background:#fff;color:var(--red);font-family:"Cabin",sans-serif;font-weight:600;font-size:16px;border-radius:3px;padding-top:5px}
.feature{top:698px;width:266px;height:102px;border:1px solid var(--line);display:flex;align-items:center;gap:10px;padding-left:13px}
.feature h3{font-family:"Cabin",sans-serif;font-weight:400;font-size:14.5px;color:#333}
.feature p{font-size:14px;color:#444;margin-top:3px}
.footer{left:0;top:842px;width:1200px;height:288px;background:linear-gradient(180deg,#f3f5f7,#e6eaee)}
.fcol h4{font-family:"Cabin",sans-serif;font-weight:600;font-size:15.5px;color:#111;padding-bottom:8px;border-bottom:1px solid #ccc}
.fcol ul{list-style:none;margin-top:10px;font-size:13.5px;color:#333}
.fcol li{height:24.5px;display:flex;align-items:center;gap:9px;white-space:nowrap}
.fcol li::before{content:"";width:5px;height:5px;border-right:1.5px solid #333;border-top:1.5px solid #333;transform:rotate(45deg)}
.news p{font-size:12px;color:#555;line-height:17px;margin-top:12px}
.subscribe{display:flex;margin-top:12px;height:32px}
.subscribe .field{width:160px;border:1px solid #ccc;background:#fff;font-size:11px;color:#666;padding:9px 8px}
.subscribe .go{width:82px;background:var(--red);color:#fff;font-size:13px;padding-top:9px;text-align:center}
.fsocial{display:flex;gap:9px;margin-top:14px}
.cards{display:flex;gap:6px;margin-top:12px}
.cards span{width:34px;height:21px;border-radius:2px;border:1px solid #bbb;position:relative}
.cards span::after{content:"";position:absolute;left:4px;right:4px;top:6px;height:3px;background:rgba(0,0,0,.25)}
.copyright{left:0;top:1130px;width:1200px;height:44px;background:var(--red);color:#fff;text-align:center;font-size:13.5px;padding-top:14px}
</style>
</head>
<body>

<header>
  <div class="abs topbar">
    <div class="abs phone">
      <svg width="17" height="17" viewBox="0 0 24 24" fill="#fff"><path d="M6.6 10.8a15 15 0 0 0 6.6 6.6l2.2-2.2c.3-.3.7-.4 1-.2 1.1.4 2.3.6 3.6.6.6 0 1 .4 1 1V20c0 .6-.4 1-1 1A17 17 0 0 1 3 4c0-.6.4-1 1-1h3.5c.6 0 1 .4 1 1 0 1.2.2 2.4.6 3.6.1.3 0 .7-.2 1z"/></svg>
      +1 555 014 2290
    </div>
    <ul class="abs toplinks">
      <li><svg width="26" height="18" viewBox="0 0 26 18" fill="none" stroke="#fff" stroke-width="1.6"><path d="M1 1h4l3 11h13l3-8H7"/><circle cx="10" cy="16" r="1.4"/><circle cx="19" cy="16" r="1.4"/></svg> View Cart (0)</li>
      <li>Checkout</li>
      <li>My Cart</li>
      <li>My Wishlist</li>
      <li><svg width="10" height="13" viewBox="0 0 10 13" fill="#fff"><rect x="0" y="5" width="10" height="8" rx="1"/><path d="M2 5V3a3 3 0 0 1 6 0" stroke="#fff" fill="none" stroke-width="1.5"/></svg> Log In</li>
      <li><svg width="13" height="13" viewBox="0 0 13 13" fill="#fff"><circle cx="6.5" cy="3.5" r="3"/><path d="M0 13a6.5 5 0 0 1 13 0z"/></svg> My Account</li>
    </ul>
  </div>

  <div class="abs brand-name">LOMA TRADE</div>
  <div class="abs brand-dot"></div>

  <div class="abs search">Search...
    <svg width="14" height="14" viewBox="0 0 14 14" fill="none" stroke="#c9413a" stroke-width="2"><circle cx="6" cy="6" r="4.5"/><path d="M9.5 9.5L13 13"/></svg>
  </div>
  <div class="abs social" aria-label="Social links">
    <span><svg width="14" height="11" viewBox="0 0 14 11" fill="none" stroke="#333" stroke-width="1.4"><rect x="1" y="1" width="12" height="9"/><path d="M1 1l6 5 6-5"/></svg></span>
    <span><svg width="14" height="13" viewBox="0 0 14 13" fill="none" stroke="#333" stroke-width="1.4"><path d="M1 1h12v8H6l-3 3V9H1z"/></svg></span>
    <span><svg width="13" height="13" viewBox="0 0 13 13" fill="none" stroke="#333" stroke-width="1.4"><circle cx="3" cy="6.5" r="2"/><circle cx="10" cy="2.5" r="2"/><circle cx="10" cy="10.5" r="2"/><path d="M5 5.5l3-2M5 7.5l3 2"/></svg></span>
    <span><svg width="13" height="13" viewBox="0 0 13 13" fill="none" stroke="#333" stroke-width="1.4"><path d="M6.5 11.5S1 8 1 4.5A2.7 2.7 0 0 1 6.5 3 2.7 2.7 0 0 1 12 4.5C12 8 6.5 11.5 6.5 11.5z"/></svg></span>
  </div>
  <div class="abs support"><svg width="13" height="13" viewBox="0 0 13 13" fill="#c9413a"><circle cx="6.5" cy="3.5" r="3"/><path d="M0 13a6.5 5 0 0 1 13 0z"/></svg> Support Online - Chat Now</div>

  <ul class="abs mainnav">
    <li class="active">Home</li><li>All Categories</li><li>Products</li><li>Sale</li><li>New Items</li><li>Other Accessories</li><li>Blog</li><li>About Us</li><li>Contact Us</li>
  </ul>
</header>

<main>
  <section class="abs hero">
    <div class="abs hero-photo" role="img" aria-label="Two women wearing colourful printed African tunics"></div>
    <h1 class="abs hero-copy">We Are A Wholesaler<br>of African-made And<br>African-themed<br>Products</h1>
    <div class="abs btn-red hero-btn">Shop Now</div>
    <div class="abs dots"><span></span><span></span><span></span><span></span></div>
  </section>

  <aside class="abs promo">
    <h2>Start your African business today!<br>Only $49.00 &amp; FREE Shipping</h2>
    <div class="abs promo-photo" role="img" aria-label="Business start-up kit of soaps, shea butter and oils"></div>
    <p class="abs p1">Get the Easy Business Start-Up Kit Today!</p>
    <p class="abs p2">Once you get the Start-Up Kit, you can immediately get new customers &amp; start selling products.</p>
    <p class="abs p3">Now is the best time to start a business &amp; earn extra money. Click here for more details.</p>
    <div class="abs promo-btn">Start Business Today</div>
  </aside>

  <div class="abs feature" style="left:165px">
    <svg width="44" height="34" viewBox="0 0 44 34" fill="#333"><rect x="14" y="2" width="28" height="22" rx="2"/><path d="M13 9H6L1 17v9h12z"/><circle cx="9" cy="28" r="4.5" stroke="#fff" stroke-width="1.5"/><circle cx="34" cy="28" r="4.5" stroke="#fff" stroke-width="1.5"/></svg>
    <div><h3>FREE DELIVERY WORLDWIDE</h3><p>On order over $ 400.00</p></div>
  </div>
  <div class="abs feature" style="left:467px">
    <svg width="42" height="40" viewBox="0 0 42 40" fill="#333"><rect x="2" y="11" width="38" height="9"/><rect x="5" y="22" width="32" height="17"/><rect x="18" y="11" width="6" height="28" fill="#fff"/><path d="M21 11c-4-9-13-9-11-3 1 2 6 3 11 3zm0 0c4-9 13-9 11-3-1 2-6 3-11 3z" fill="none" stroke="#333" stroke-width="3"/></svg>
    <div><h3>DISCOUNT ON ORDER GIFT</h3><p>At vero eos accusamus iusto</p></div>
  </div>
  <div class="abs feature" style="left:763px">
    <svg width="42" height="44" viewBox="0 0 42 44" fill="#333"><circle cx="18" cy="13" r="8"/><path d="M8 14a10 10 0 0 1 20 0" fill="none" stroke="#333" stroke-width="2.5"/><path d="M2 44c0-12 7-18 16-18s16 6 16 18z"/><circle cx="33" cy="36" r="7" fill="#555" stroke="#fff" stroke-width="1.5"/><path d="M30 33l6 6M36 33l-6 6" stroke="#fff" stroke-width="1.8"/></svg>
    <div><h3>CUSTOMER SUPPORT</h3><p>We Are Here For You!</p></div>
  </div>
</main>

<footer>
  <div class="abs footer"></div>

  <div class="abs fcol news" style="left:100px;top:876px;width:245px">
    <h4>Newsletter Sign-up</h4>
    <p>Lorem ipsum dolor sit amet, consecte lorem adipiscing elit sed diamr</p>
    <div class="subscribe"><div class="field">Enter your Email Address</div><div class="go">SUBSCRIBE</div></div>
  </div>
  <div class="abs fcol" style="left:100px;top:1017px;width:239px">
    <h4 style="padding-left:3px">Follow Us On</h4>
    <div class="fsocial" aria-label="Social links">
      <span><svg width="14" height="11" viewBox="0 0 14 11" fill="none" stroke="#333" stroke-width="1.4"><rect x="1" y="1" width="12" height="9"/><path d="M1 1l6 5 6-5"/></svg></span>
      <span><svg width="14" height="13" viewBox="0 0 14 13" fill="none" stroke="#333" stroke-width="1.4"><path d="M1 1h12v8H6l-3 3V9H1z"/></svg></span>
      <span><svg width="13" height="13" viewBox="0 0 13 13" fill="none" stroke="#333" stroke-width="1.4"><circle cx="3" cy="6.5" r="2"/><circle cx="10" cy="2.5" r="2"/><circle cx="10" cy="10.5" r="2"/><path d="M5 5.5l3-2M5 7.5l3 2"/></svg></span>
      <span><svg width="13" height="13" viewBox="0 0 13 13" fill="none" stroke="#333" stroke-width="1.4"><path d="M6.5 11.5S1 8 1 4.5A2.7 2.7 0 0 1 6.5 3 2.7 2.7 0 0 1 12 4.5C12 8 6.5 11.5 6.5 11.5z"/></svg></span>
    </div>
  </div>

  <div class="abs fcol" style="left:430px;top:876px;width:134px">
    <h4>Quick Links</h4>
    <ul><li>Home</li><li>All Categories</li><li>Products</li><li>Sale</li><li>New Items</li><li>Other Accessories</li><li>About Us</li><li>Contact Us</li></ul>
  </div>

  <div class="abs fcol" style="left:632px;top:876px;width:196px">
    <h4>More About Loma Trade</h4>
    <ul><li>About Loma Trade</li><li>How We Help Africa</li><li>African Proverbs</li><li>Free Articles</li><li>How Can We Improve?</li></ul>
  </div>
  <div class="abs fcol" style="left:634px;top:1049px;width:196px">
    <h4 style="padding-bottom:4px">Payments Options</h4>
    <div class="cards" aria-label="Accepted payment cards"><span style="background:#f4f4f4"></span><span style="background:#1d2a5a"></span><span style="background:#f4f4f4"></span><span style="background:#2f7fc9"></span><span style="background:#f3e3b0"></span></div>
  </div>

  <div class="abs fcol" style="left:914px;top:876px;width:182px">
    <h4>Shipping &amp; Returns</h4>
    <ul><li>Standard Return Policy</li><li>Shipping Policy</li><li>Delivery Policies</li></ul>
  </div>
  <div class="abs fcol" style="left:914px;top:1031px;width:182px">
    <h4>Make Money With Us</h4>
    <ul><li>Lorem&nbsp; Ispum is the dummy</li><li>Lorem Ispum</li></ul>
  </div>

  <div class="abs copyright">Copyright © 2017 Loma Trade. All Rights Reserved.</div>
</footer>

</body>
</html>
```